New International Co-Working Space Needs Pre-Registration Website

We need a simple but stylish pre-registration website for Nordcrest, a new international Coworking space. It needs to feature four sections: a description of the space, the benefits, the offering and a pre-registration form. We are looking for a clean, modern and simple yet stylish design. The site needs to be based on the divi wordpress theme. I have attached a more thorough briefing as well as our logo and some pictures we want to use.

Coding

Coded - Design and coding required

Number of Pages Required

3 page

```html
<!DOCTYPE html>
<html lang="en">
<head>
<meta charset="utf-8">
<title>Nordcrest – Coworking Space</title>
<link href="https://fonts.googleapis.com/css2?family=Roboto:ital,wght@0,400;0,500;0,700;1,700&family=Open+Sans:ital,wght@0,400;0,600;1,700&display=swap" rel="stylesheet">
<style>
:root{
  --yellow:#f2b61f;
  --yellow-dark:#e0a50e;
  --ink:#222222;
  --text:#333333;
  --dark:#232323;
  --dark-2:#1b1b1b;
  --white:#ffffff;
  --light:#f7f7f7;
  --muted:#777777;
}
*{box-sizing:border-box;margin:0;padding:0}
html,body{width:1200px;height:3719px;overflow:hidden}
body{position:relative;background:var(--white);font-family:"Open Sans",Arial,sans-serif;color:var(--text)}
.abs{position:absolute}
h2.section-title{position:absolute;left:0;width:1200px;text-align:center;font-family:"Roboto",Arial,sans-serif;font-weight:700;font-size:34px;letter-spacing:.5px}

/* hero */
.hero{left:0;top:0;width:1200px;height:657px;background:linear-gradient(180deg,#4b4e52 0%,#3a3633 45%,#2a1f1a 100%)}
.hero-shade{left:0;top:0;width:1200px;height:657px;background:radial-gradient(ellipse at 50% 40%,rgba(120,120,120,.25),rgba(0,0,0,.35))}
.brand{left:99px;top:40px;display:flex;align-items:center;gap:14px;font-family:"Roboto",Arial,sans-serif;font-weight:700;font-size:46px;color:var(--white);line-height:1}
.brand-dot{width:46px;height:46px;border-radius:50%;background:var(--yellow)}
.btn-contact{left:838px;top:27px;width:106px;height:35px;background:var(--yellow);color:var(--ink);font-family:"Roboto",Arial,sans-serif;font-weight:700;font-size:16px;display:flex;align-items:center;justify-content:center}
.lang{left:964px;top:34px;font-family:"Roboto",Arial,sans-serif;font-weight:500;font-size:15px;color:var(--white)}
.lang .on{color:var(--yellow)}
.main-nav{left:461px;top:86px;display:flex;gap:22px;font-family:"Roboto",Arial,sans-serif;font-weight:700;font-size:14px;color:var(--white)}
.main-nav .on{color:var(--yellow)}
.hero-mark{left:530px;top:216px;width:140px;height:140px;border-radius:50%;background:var(--yellow)}
.hero-title{left:0;top:380px;width:1200px;text-align:center;font-family:"Roboto",Arial,sans-serif;font-style:italic;font-weight:700;font-size:42px;line-height:54px;color:var(--white);text-shadow:0 2px 6px rgba(0,0,0,.5)}
.dots{left:570px;top:517px;display:flex;gap:8px}
.dots span{width:12px;height:12px;border-radius:50%;border:2px solid var(--white)}
.dots span.on{background:var(--white)}

/* about */
.about-mark{left:564px;top:728px;width:72px;height:72px;border-radius:50%;background:var(--ink)}
.about-title{top:820px;color:var(--ink);font-size:38px}
.about-text{left:144px;width:912px;text-align:center;font-size:12.5px;line-height:22px;color:var(--text)}
.about-quote{left:0;top:940px;width:1200px;text-align:center;font-family:"Open Sans",Arial,sans-serif;font-style:italic;font-weight:700;font-size:27px;color:var(--yellow)}

/* space */
.space{left:0;top:1135px;width:1200px;height:583px;background:var(--dark)}
.space-title{top:1196px;color:var(--white)}
.space-card{top:1291px;width:305px}
.space-photo{width:305px;height:191px;border:3px solid var(--white)}
.space-caption{margin-top:18px;text-align:right;padding-right:12px;font-family:"Roboto",Arial,sans-serif;font-weight:500;font-size:17px;color:var(--white)}
.space-text{margin-top:18px;font-size:12.5px;line-height:20px;color:#dddddd}

/* goodies */
.goodies{left:0;top:1718px;width:1200px;height:582px;background:var(--yellow)}
.goodies-hexes{left:30px;top:1795px}
.goodies-title{left:667px;top:1818px;font-family:"Roboto",Arial,sans-serif;font-weight:700;font-size:33px;color:var(--ink)}
.goodies-text{left:667px;top:1874px;width:440px;font-size:13px;line-height:22px;color:var(--white)}
.benefits-title{left:667px;top:1975px;font-family:"Roboto",Arial,sans-serif;font-weight:700;font-size:24px;color:var(--ink)}
.benefits{left:667px;top:2026px;list-style:none}
.benefits li{display:flex;align-items:center;gap:14px;height:34px;font-size:14.5px;color:var(--ink)}
.benefits li::before{content:"";width:14px;height:14px;border-radius:50%;border:2px solid var(--ink)}

/* offering */
.offer-title{top:2362px;color:var(--ink)}
.offer-card{top:2467px;width:309px}
.offer-photo{width:309px;height:178px}
.offer-date{position:absolute;left:0;top:-12px;width:100px;height:30px;background:var(--yellow);color:var(--ink);font-family:"Roboto",Arial,sans-serif;font-weight:500;font-size:14px;display:flex;align-items:center;justify-content:center}
.offer-text{margin-top:22px;font-size:12.5px;line-height:21px;color:var(--text)}

/* register */
.register{left:0;top:2826px;width:1200px;height:526px;background:linear-gradient(135deg,#2b2522 0%,#3a3330 40%,#231e1b 100%)}
.register-title{top:2898px;color:var(--white)}
.field{border:2px solid var(--white);color:var(--white);font-size:11px;padding:0 12px;display:flex;align-items:center}
.field.area{align-items:flex-start;padding-top:12px}
.btn-register{left:481px;top:3230px;width:238px;height:42px;background:var(--yellow);color:var(--ink);font-family:"Roboto",Arial,sans-serif;font-weight:700;font-size:17px;display:flex;align-items:center;justify-content:center}

/* footer */
.footer{left:0;top:3352px;width:1200px;height:302px;background:var(--light)}
.foot-brand{left:99px;top:3424px;display:flex;align-items:center;gap:12px;font-family:"Roboto",Arial,sans-serif;font-weight:700;font-size:40px;color:var(--ink);line-height:1}
.foot-brand .brand-dot{width:40px;height:40px;background:var(--ink)}
.social{left:188px;top:3496px;display:flex;gap:6px}
.social span{width:24px;height:24px;border-radius:50%;border:1.5px solid var(--ink)}
.foot-head{font-family:"Roboto",Arial,sans-serif;font-weight:500;font-size:18px;color:var(--ink);letter-spacing:.3px}
.foot-text{font-size:11.5px;line-height:19px;color:var(--text)}
.email-input{left:377px;top:3500px;width:243px;height:38px;border:1px solid #cccccc;background:var(--white);font-size:11px;color:var(--muted);display:flex;align-items:center;padding-left:12px}
.btn-sub{left:377px;top:3550px;width:131px;height:35px;background:var(--yellow);color:var(--ink);font-family:"Roboto",Arial,sans-serif;font-weight:700;font-size:13px;display:flex;align-items:center;justify-content:center}
.contact-item{left:694px;display:flex;gap:12px;font-size:12px;line-height:19px;color:var(--text)}
.quick-links{left:989px;top:3450px;list-style:none;font-size:12px;line-height:26px;color:var(--text)}
.copyright{left:0;top:3654px;width:1200px;height:65px;border-top:1px solid #e2e2e2;background:var(--white);display:flex;align-items:center;justify-content:center;font-size:12px;color:var(--text)}
</style>
</head>
<body>

<!-- Hero -->
<div class="abs hero" role="img" aria-label="Photo of an open coworking office with people working at laptops"></div>
<div class="abs hero-shade"></div>
<div class="abs brand"><span class="brand-dot"></span>nordcrest</div>
<div class="abs btn-contact">CONTACT</div>
<div class="abs lang">GERMAN | <span class="on">ENGLISH</span></div>
<nav class="abs main-nav">
  <span class="on">HOME</span><span>THE BEAUTIFUL SPACE</span><span>ALL THE GOODIES</span><span>THE OFFERING</span><span>PRE-REGISTER NOW!</span>
</nav>
<div class="abs hero-mark"></div>
<h1 class="abs hero-title">FOCUS ON YOUR WORK.<br>AND LEAVE THE REST TO US.</h1>
<div class="abs dots"><span class="on"></span><span></span><span></span></div>

<!-- About -->
<div class="abs about-mark"></div>
<h2 class="section-title about-title">ABOUT NORDCREST</h2>
<p class="abs about-text" style="top:878px">Nordcrest is a new plug &amp; play Coworking Space that offers startups and corporations flexible and inspiring office space together with leading-edge professional services. This allows them to exclusively focus on bringing their innovative ideas to life – without having to worry about anything else.</p>
<p class="abs about-quote">Focus on your work. And leave the rest to us</p>
<p class="abs about-text" style="top:996px">Nordcrest features a marketing &amp; digital technology (MarTech) consultancy – Brightloop Inc. (working title) – as well as various service companies and professionals. They support the startups and corporate coworkers on their projects; from target group research to branding strategy, from service design to customer acquisition, from proof-of-concept to near shore development, from fiduciary services to legal support.</p>

<!-- Beautiful space -->
<div class="abs space"></div>
<h2 class="section-title space-title">THE BEAUTIFUL SPACE</h2>
<div class="abs space-card" style="left:99px">
  <div class="space-photo" role="img" aria-label="Photo of a team working around a desk" style="background:linear-gradient(135deg,#d8d2cc,#8a3b34 55%,#3d2a24)"></div>
  <div class="space-caption">Phasellus at quam trist</div>
  <p class="space-text">Sed ut perspiciatis unde omnis iste natus error sit voluptatem accusantium doloremque laudantium, tam rem aperiam, eaque ipsa quae ab illo intore veritatis et quasi architecto beatae</p>
</div>
<div class="abs space-card" style="left:446px">
  <div class="space-photo" role="img" aria-label="Photo of a busy shared workspace" style="background:linear-gradient(135deg,#b9b9b6,#5d5e60 55%,#2a2a2c)"></div>
  <div class="space-caption">Phasellus at quam trist</div>
  <p class="space-text">Sed ut perspiciatis unde omnis iste natus error sit voluptatem accusantium doloremque laudantium, tam rem aperiam, eaque ipsa quae ab illo intore veritatis et quasi architecto beatae</p>
</div>
<div class="abs space-card" style="left:793px">
  <div class="space-photo" role="img" aria-label="Photo of hands writing notes at a meeting table" style="background:linear-gradient(135deg,#c9b7a6,#7a2c28 55%,#2e211c)"></div>
  <div class="space-caption">Phasellus at quam trist</div>
  <p class="space-text">Sed ut perspiciatis unde omnis iste natus error sit voluptatem accusantium doloremque laudantium, tam rem aperiam, eaque ipsa quae ab illo intore veritatis et quasi architecto beatae</p>
</div>

<!-- Goodies -->
<div class="abs goodies"></div>
<svg class="abs goodies-hexes" width="600" height="420" viewBox="0 0 600 420">
  <g stroke="#ffffff" stroke-width="6">
    <polygon role="img" aria-label="Photo of branded notebook and pen" fill="#5a5a5a" points="187,115 242,20 352,20 407,115 352,210 242,210"/>
    <polygon role="img" aria-label="Photo of branded pens" fill="#8c8c8c" points="14,220 69,125 179,125 234,220 179,315 69,315"/>
    <polygon role="img" aria-label="Photo of a branded hoodie" fill="#d9d9d9" points="367,210 422,115 532,115 587,210 532,305 422,305"/>
    <polygon role="img" aria-label="Photo of a branded coffee mug" fill="#eeeeee" points="189,318 244,223 354,223 409,318 354,413 244,413"/>
  </g>
</svg>
<h2 class="abs goodies-title">ALL THE GOODIES</h2>
<p class="abs goodies-text">Sed ut perspiciatis unde omnis iste natus error sit voluptatem accusantium doloremque laudantium, totam rem aperiam, eaque ipsa quae ab illo inventore veritatis et quasi architecto beatae vitae</p>
<h3 class="abs benefits-title">BENEFITS</h3>
<ul class="abs benefits">
  <li>Aenean a est non lectus maximus laoreet.</li>
  <li>Quisque quis eros quis odio posuere dapibus.</li>
  <li>Mauris vestibulum tellus at consectetur sodales.</li>
  <li>Ut et urna porttitor, hendrerit dui vitae, luctus augue.</li>
  <li>Nunc in mauris vehicula elit viverra aliquam quis nec elit.</li>
</ul>

<!-- Offering -->
<h2 class="section-title offer-title">THE OFFERING</h2>
<div class="abs offer-card" style="left:99px">
  <div class="offer-photo" role="img" aria-label="Photo of fresh croissants and pastries" style="background:linear-gradient(135deg,#e2a05a,#a8521f 55%,#4a2412)"></div>
  <div class="offer-date">SEP 09 2017</div>
  <p class="offer-text">Sed ut perspiciatis unde omnis iste natus error sit uatem accusantium doloremque laudantium, totam rem aperiam, eaque ipsa quae</p>
</div>
<div class="abs offer-card" style="left:446px">
  <div class="offer-photo" role="img" aria-label="Photo of a coffee bar with a lit sign" style="background:linear-gradient(180deg,#2a2624,#5e3f2a 60%,#1d1a18)"></div>
  <div class="offer-date">SEP 09 2017</div>
  <p class="offer-text">Sed ut perspiciatis unde omnis iste natus error sit uatem accusantium doloremque laudantium, totam rem aperiam, eaque ipsa quae</p>
</div>
<div class="abs offer-card" style="left:791px">
  <div class="offer-photo" role="img" aria-label="Photo of an espresso machine pouring coffee" style="background:linear-gradient(135deg,#1e1e1e,#4a4644 55%,#c8c4c0)"></div>
  <div class="offer-date">SEP 09 2017</div>
  <p class="offer-text">Sed ut perspiciatis unde omnis iste natus error sit uatem accusantium doloremque laudantium, totam rem aperiam, eaque ipsa quae</p>
</div>

<!-- Pre-register -->
<div class="abs register" role="img" aria-label="Dimmed photo of a person writing at a desk"></div>
<h2 class="section-title register-title">PRE-REGISTER NOW!</h2>
<div class="abs field" style="left:250px;top:2987px;width:338px;height:35px">Full Name*</div>
<div class="abs field" style="left:610px;top:2987px;width:337px;height:35px">E-Mail Address*</div>
<div class="abs field" style="left:250px;top:3039px;width:338px;height:35px">Company Name*</div>
<div class="abs field" style="left:610px;top:3039px;width:337px;height:35px">Phone Number*</div>
<div class="abs field area" style="left:250px;top:3091px;width:697px;height:112px">Message*</div>
<div class="abs btn-register">PRE-REGISTER NOW!</div>

<!-- Footer -->
<div class="abs footer"></div>
<div class="abs foot-brand"><span class="brand-dot"></span>nordcrest</div>
<div class="abs social" aria-label="Social links"><span></span><span></span><span></span><span></span></div>

<h4 class="abs foot-head" style="left:377px;top:3403px">SIGN UP FOR NEWSLETTER</h4>
<p class="abs foot-text" style="left:377px;top:3448px;width:240px">Excepteur sint occaecat cupidatat non proident, sunt in culpa qui officia deserunt</p>
<div class="abs email-input">Enter email</div>
<div class="abs btn-sub">SUBSCRIPTION</div>

<h4 class="abs foot-head" style="left:694px;top:3403px">CONTACT US</h4>
<div class="abs contact-item" style="top:3454px">
  <svg width="12" height="16" viewBox="0 0 12 16"><path d="M6 0C2.7 0 0 2.6 0 5.9 0 10 6 16 6 16s6-6 6-10.1C12 2.6 9.3 0 6 0zm0 8.2A2.3 2.3 0 1 1 6 3.6a2.3 2.3 0 0 1 0 4.6z" fill="#f2b61f"/></svg>
  <span>Nordcrest<br>48 W. Alder Lane Fairbrook,<br>NJ 07999</span>
</div>
<div class="abs contact-item" style="top:3528px">
  <svg width="12" height="14" viewBox="0 0 12 14"><path d="M2.5 0.5l2 3-1.2 1.4c.8 1.8 2 3 3.8 3.8L8.5 7.5l3 2-1 2.6C5.3 12 0 6.7 0 1.5z" fill="#f2b61f"/></svg>
  <span>Phone: (555) 014-2290</span>
</div>
<div class="abs contact-item" style="top:3558px">
  <svg width="14" height="12" viewBox="0 0 14 12"><rect x="0.5" y="1.5" width="13" height="9" fill="#f2b61f"/><path d="M0.5 1.5l6.5 5 6.5-5" stroke="#ffffff" fill="none"/></svg>
  <span>info@nordcrest.com</span>
</div>

<h4 class="abs foot-head" style="left:989px;top:3403px">QUICK LINKS</h4>
<ul class="abs quick-links">
  <li>Home</li><li>The beautiful space</li><li>All the goodies</li><li>The offering</li><li>Pre-register now!</li>
</ul>

<div class="abs copyright">©Nordcrest AG Zurich</div>

</body>
</html>
```